LINGERIE WEBSHOP - Velora casa

We are looking for design and layout design for our webshop. We are company that sells lingerie and other connected textile products liki payamas and etc..
Our website will have approx 500 different products within 2 main catogories Woman/Man) and approx. 10 subcategories
Here is what we expect form design:
-Color pallete should be black and white (if you wish you can add some accent color)
-we want to leave feeling to customers of good quality products towards to luxury
-UX should be simple. Feel free to suggest layout
-frontpage layout, product list layout, product description layout, blog layout
-responsive design, compatible with smartphone

Target Market(s)

woman buying for themself, man buying for woman

Industry/Entity Type

Lingerie

Logo Text

VELORA CASA

Number of Pages Required

4 page

Font styles to use
Sans Serif
Decorative

Requirements
Must have
• simple UX
Nice to have
• difference for sexy/luxury lingerie and daily/cozy lingerie
Should not have
• cheap feel, unreliable

```html
<!DOCTYPE html>
<html lang="en">
<head>
<meta charset="utf-8">
<title>Velora casa — Lingerie &amp; Sleepwear</title>
<link href="https://fonts.googleapis.com/css2?family=Montserrat:wght@400;500;600;700&family=Tinos:ital@0;1&family=Dancing+Script:wght@600&display=swap" rel="stylesheet">
<style>
:root{
  --gold:#c8955a;
  --ink:#1e1e1e;
  --text:#444;
  --muted:#8a8a8a;
  --line:#e2e2e2;
  --lav:#efeefa;
  --soft:#f6f6f9;
  --footer:#262631;
  --tab:#b8b8b8;
}
*{box-sizing:border-box;margin:0;padding:0}
html,body{width:1200px;height:3934px;overflow:hidden;background:#fff}
body{position:relative;font-family:"Montserrat",sans-serif;color:var(--text)}
.abs{position:absolute}
.serif{font-family:"Tinos",serif}
/* hero */
.hero{left:0;top:0;width:1200px;height:550px;background:linear-gradient(90deg,#6b6e72 0%,#8a5a5c 35%,#9a3a40 48%,#7a5a58 62%,#6e7072 100%)}
.hero-shade{inset:0;background:linear-gradient(180deg,rgba(0,0,0,.25),rgba(0,0,0,.05) 40%,rgba(60,50,30,.2))}
.nav{top:30px;height:30px;display:flex;align-items:center;gap:12px;color:#fff;font-size:12px;letter-spacing:2px;font-weight:500;border-bottom:1px solid var(--gold);padding-bottom:8px}
.nav .dot{width:4px;height:4px;border-radius:50%;background:#fff;display:inline-block}
.logo{left:0;width:1200px;top:30px;text-align:center;font-family:"Tinos",serif;color:#222;font-size:36px;letter-spacing:1px}
.hero-kicker{top:190px;width:1200px;text-align:center;color:#fff;font-size:14px;letter-spacing:3px}
.hero-title{top:232px;width:1200px;text-align:center;color:#fff;font-family:"Dancing Script",cursive;font-size:64px}
.hero-sub{top:302px;width:1200px;text-align:center;color:#fff;font-family:"Tinos",serif;font-size:38px}
.hero-sub span{color:var(--gold)}
.btn-gold{background:var(--gold);color:#fff;font-weight:700;font-size:12px;display:flex;align-items:center;justify-content:center;letter-spacing:.5px}
.dots{top:514px;left:568px;display:flex;gap:7px}
.dots i{width:7px;height:7px;border-radius:50%;border:1px solid #fff;display:block}
.dots i:first-child{background:#fff}
/* features */
.features{left:102px;top:599px;width:995px;height:154px;background:var(--lav)}
.feat-title{font-family:"Tinos",serif;font-size:17px;color:#222}
.feat-text{font-size:10px;line-height:14px;color:#777;width:210px}
/* promos */
.promo{top:864px;width:463px;height:316px;background:linear-gradient(135deg,#4c4c4c,#262626)}
.promo-photo{top:0;left:0;height:316px}
.promo-title{right:18px;top:70px;font-family:"Tinos",serif;color:#fff;font-size:25px;text-align:right;letter-spacing:.5px}
.promo-off{right:20px;top:106px;color:#ddd;font-size:15px;letter-spacing:4px}
.btn-line{border:2px solid var(--gold);color:#fff;font-size:12px;font-weight:700;display:flex;align-items:center;justify-content:center;width:155px;height:54px;right:17px;top:170px}
/* headings */
.sec-head{width:1200px;text-align:center;font-family:"Tinos",serif;font-size:23px;color:#222;display:flex;justify-content:center;align-items:center;gap:48px}
.sec-head i{display:block;width:42px;height:2px;background:#777}
.sec-head.wide{gap:20px}.sec-head.wide i{width:75px}
/* tabs */
.tab{top:1379px;height:36px;width:122px;font-size:11px;letter-spacing:2px;color:#fff;font-weight:600;display:flex;align-items:center;padding-left:12px;background:var(--tab);clip-path:polygon(0 0,82% 0,100% 100%,0 100%)}
.tab.active{background:#000}
/* cards */
.card{width:234px;height:351px;border:1px solid var(--line);background:#fff}
.card-img{left:0;top:0;width:232px;height:240px}
.card-name{top:256px;width:100%;text-align:center;font-family:"Tinos",serif;font-size:13px;color:#555}
.card-price{top:280px;width:100%;text-align:center;font-size:12px;font-weight:700;color:#222}
.card-link{top:314px;width:100%;display:flex;justify-content:center;align-items:center;gap:10px;font-size:10px;letter-spacing:3px;color:#555}
.badge{top:0;left:0;background:#000;color:#fff;font-size:10px;letter-spacing:2px;height:34px;width:90px;padding:11px 0 0 6px;clip-path:polygon(0 0,100% 0,78% 100%,0 100%)}
.pager{display:flex;gap:2px}
.pager span{width:31px;height:31px;background:var(--gold);display:flex;align-items:center;justify-content:center}
/* summer */
.summer{left:102px;top:1944px;width:995px;height:342px;background:radial-gradient(ellipse at 50% 30%,#4a4a4a,#262626 70%)}
.summer-title{top:106px;width:995px;text-align:center;font-family:"Tinos",serif;color:#fff;font-size:31px}
.summer-sub{top:158px;width:995px;text-align:center;color:#eee;font-size:12px;letter-spacing:4px}
/* testimonials */
.testi{left:0;top:3020px;width:1200px;height:523px;background:var(--soft)}
.center{width:1200px;text-align:center}
/* footer */
.footer{left:0;top:3543px;width:1200px;height:391px;background:var(--footer);color:#fff}
.f-head{top:82px;font-family:"Tinos",serif;font-size:17px;border-bottom:1px solid #fff;padding-bottom:2px}
.f-list{top:138px;list-style:none;font-size:10px;letter-spacing:1.5px}
.f-list li{height:34px;display:flex;align-items:flex-start;gap:10px}
.f-list svg{margin-top:2px}
</style>
</head>
<body>

<!-- HERO -->
<section class="abs hero" role="img" aria-label="Woman in a red printed pajama set standing outdoors with arms outstretched">
  <div class="abs hero-shade"></div>
</section>
<nav class="abs nav" style="left:114px;width:318px">HOME <i class="dot"></i> SHOP <i class="dot"></i> PRODUCTS <i class="dot"></i> REVIEWS</nav>
<div class="abs logo">VELORA CASA</div>
<nav class="abs nav" style="left:773px;width:327px">BLOG <i class="dot"></i> TRENDY <i class="dot"></i> MY ACCOUNT <i class="dot"></i>
  <svg width="20" height="16" viewBox="0 0 20 16" fill="none" stroke="#fff" stroke-width="1.3"><path d="M1 1h3l2 10h10l2-7H5"/><circle cx="8" cy="14" r="1.2"/><circle cx="15" cy="14" r="1.2"/></svg>(3)</nav>
<div class="abs hero-kicker">END OF SEASON</div>
<div class="abs hero-title">Close Out Sale</div>
<div class="abs hero-sub">UPTO <span>25% OFF</span></div>
<a class="abs btn-gold" style="left:522px;top:376px;width:155px;height:52px">TAKE A LOOK</a>
<div class="abs dots"><i></i><i></i><i></i><i></i><i></i></div>

<!-- FEATURES -->
<section class="abs features">
  <svg class="abs" style="left:48px;top:42px" width="50" height="40" viewBox="0 0 50 40" fill="none" stroke="#555" stroke-width="2.5"><rect x="3" y="4" width="26" height="24" rx="3"/><path d="M29 12h10l7 8v8H29z"/><circle cx="12" cy="32" r="4"/><circle cx="38" cy="32" r="4"/><circle cx="16" cy="14" r="5"/><path d="M16 11v3h2"/></svg>
  <div class="abs feat-title" style="left:122px;top:38px">FAST DELIVERY</div>
  <div class="abs feat-text" style="left:122px;top:70px">Lorem ipsum dolor sit amet, conse ctetur ad ipiscing elit, sed do eiusmod tempor incidi du nt ut lua.</div>
  <svg class="abs" style="left:364px;top:42px" width="48" height="48" viewBox="0 0 48 48" fill="none" stroke="#555" stroke-width="3"><path d="M9 24a15 15 0 0 1 30 0"/><rect x="6" y="22" width="7" height="11" rx="2" fill="#555"/><rect x="35" y="22" width="7" height="11" rx="2" fill="#555"/><circle cx="24" cy="28" r="11"/><path d="M38 33c0 7-6 9-12 9"/></svg>
  <div class="abs feat-title" style="left:438px;top:38px">SUPPORT</div>
  <div class="abs feat-text" style="left:438px;top:70px">Lorem ipsum dolor sit amet, conse ctetur ad ipiscing elit, sed do eiusmod tempor incidi du nt ut lua.</div>
  <svg class="abs" style="left:680px;top:42px" width="50" height="50" viewBox="0 0 50 50" fill="none" stroke="#555" stroke-width="2.5"><circle cx="8" cy="8" r="5"/><circle cx="8" cy="22" r="5"/><path d="M12 11l14 10M12 19l14-10"/><path d="M26 14h18v28H6v-12" stroke-dasharray="5 4"/></svg>
  <div class="abs feat-title" style="left:756px;top:38px">ATTRACTIVE OFFERS</div>
  <div class="abs feat-text" style="left:756px;top:70px">Lorem ipsum dolor sit amet, conse ctetur ad ipiscing elit, sed do eiusmod tempor incidi du nt ut lua.</div>
</section>

<!-- PROMO BANNERS -->
<section class="abs promo" style="left:102px">
  <div class="abs promo-photo" role="img" aria-label="Man wearing plaid flannel pajama trousers" style="width:226px;background:linear-gradient(90deg,#59607a,#8a8fa2 45%,#4e5470)"></div>
  <div class="abs promo-title">MAN’S PAJAMAS</div>
  <div class="abs promo-off">%50 OFF</div>
  <a class="abs btn-line">TAKE A LOOK</a>
</section>
<section class="abs promo" style="left:635px">
  <div class="abs promo-photo" role="img" aria-label="Woman in a peach satin pajama set" style="width:200px;background:linear-gradient(90deg,#e9a99a,#f3c2b4 50%,#d99182)"></div>
  <div class="abs promo-title">WOMAN’S PAJAMAS</div>
  <div class="abs promo-off">%50 OFF</div>
  <a class="abs btn-line">TAKE A LOOK</a>
</section>

<!-- SHOP OUR PRODUCTS -->
<h2 class="abs sec-head" style="top:1300px"><i></i>SHOP OUR PRODUCTS<i></i></h2>
<div class="abs tab active" style="left:102px">LINGERIE</div>
<div class="abs tab" style="left:206px">CATEGORY 2</div>
<div class="abs tab" style="left:333px">CATEGORY 3</div>
<div class="abs tab" style="left:460px">CATEGORY 4</div>
<div class="abs tab" style="left:587px">CATEGORY 5</div>

<article class="abs card" style="left:102px;top:1446px">
  <div class="abs card-img" role="img" aria-label="Woman in a champagne satin pajama set" style="background:linear-gradient(180deg,#d8cfc6,#b8a99a)"></div>
  <div class="abs card-name">WOMEN CASUAL LINGERIE</div><div class="abs card-price">$49</div>
  <div class="abs card-link">SHOP NOW <svg width="16" height="8" viewBox="0 0 16 8" fill="none" stroke="#555"><path d="M0 4h15M11 1l4 3-4 3"/></svg></div>
</article>
<article class="abs card" style="left:356px;top:1446px">
  <div class="abs card-img" role="img" aria-label="Woman in a pink polka dot pajama set" style="background:linear-gradient(180deg,#f1f1f1,#f08080 40%,#ee7070)"></div>
  <div class="abs badge">SALE %50</div>
  <div class="abs card-name">WOMEN CASUAL LINGERIE</div><div class="abs card-price">$49</div>
  <div class="abs card-link">SHOP NOW <svg width="16" height="8" viewBox="0 0 16 8" fill="none" stroke="#555"><path d="M0 4h15M11 1l4 3-4 3"/></svg></div>
</article>
<article class="abs card" style="left:609px;top:1446px">
  <div class="abs card-img" role="img" aria-label="Woman in a black and white check nightshirt" style="background:linear-gradient(180deg,#e8e8e8,#6e6e6e 50%,#cfcfcf)"></div>
  <div class="abs card-name">WOMEN CASUAL LINGERIE</div><div class="abs card-price">$49</div>
  <div class="abs card-link">SHOP NOW <svg width="16" height="8" viewBox="0 0 16 8" fill="none" stroke="#555"><path d="M0 4h15M11 1l4 3-4 3"/></svg></div>
</article>
<article class="abs card" style="left:863px;top:1446px">
  <div class="abs card-img" role="img" aria-label="Woman in an olive camisole and wide trousers" style="background:linear-gradient(180deg,#ededed,#7b6e5c 40%,#8a7c68)"></div>
  <div class="abs badge">SALE %50</div>
  <div class="abs card-name">WOMEN CASUAL LINGERIE</div><div class="abs card-price">$49</div>
  <div class="abs card-link">SHOP NOW <svg width="16" height="8" viewBox="0 0 16 8" fill="none" stroke="#555"><path d="M0 4h15M11 1l4 3-4 3"/></svg></div>
</article>
<div class="abs pager" style="left:568px;top:1843px">
  <span><svg width="10" height="14" viewBox="0 0 10 14" fill="none" stroke="#fff" stroke-width="1.5"><path d="M8 1L2 7l6 6"/></svg></span>
  <span><svg width="10" height="14" viewBox="0 0 10 14" fill="none" stroke="#fff" stroke-width="1.5"><path d="M2 1l6 6-6 6"/></svg></span>
</div>

<!-- SUMMER BANNER -->
<section class="abs summer">
  <div class="abs" role="img" aria-label="Folded pink striped pajama set with a coral sleep mask" style="left:376px;top:64px;width:240px;height:278px;background:linear-gradient(160deg,#f6c2c4,#ef9aa0 50%,#f7d6d6);border-radius:8px"></div>
  <div class="abs summer-title">SUMMER SEASON SALE, ON LY $39</div>
  <div class="abs summer-sub">NOT ITS YOUR TURN TO SHO. LOREM IPSUM DOLOR.</div>
  <a class="abs" style="left:422px;top:220px;width:153px;height:49px;background:#fff;color:#222;font-size:12px;font-weight:700;display:flex;align-items:center;justify-content:center">SHOP NOW</a>
</section>

<!-- LATEST PRODUCTS -->
<h2 class="abs sec-head wide" style="top:2405px"><i></i>LATEST PRODUCTS<i></i></h2>
<article class="abs card" style="left:102px;top:2500px">
  <div class="abs card-img" role="img" aria-label="White lace nightgown on a hanger" style="background:linear-gradient(180deg,#f4f1ec,#e6dfd6)"></div>
  <div class="abs card-name">WOMEN CASUAL LINGERIE</div><div class="abs card-price">$49</div>
  <div class="abs card-link">SHOP NOW <svg width="16" height="8" viewBox="0 0 16 8" fill="none" stroke="#555"><path d="M0 4h15M11 1l4 3-4 3"/></svg></div>
</article>
<article class="abs card" style="left:356px;top:2500px">
  <div class="abs card-img" role="img" aria-label="Woman in a pink polka dot pajama set" style="background:linear-gradient(180deg,#f1f1f1,#f08080 40%,#ee7070)"></div>
  <div class="abs card-name">WOMEN CASUAL LINGERIE</div><div class="abs card-price">$49</div>
  <div class="abs card-link">SHOP NOW <svg width="16" height="8" viewBox="0 0 16 8" fill="none" stroke="#555"><path d="M0 4h15M11 1l4 3-4 3"/></svg></div>
</article>
<article class="abs card" style="left:609px;top:2500px">
  <div class="abs card-img" role="img" aria-label="Folded pink striped pajamas with a sleep mask" style="background:linear-gradient(160deg,#fbe3e3,#f3a9ad 50%,#fadcdc)"></div>
  <div class="abs card-name">WOMEN CASUAL LINGERIE</div><div class="abs card-price">$49</div>
  <div class="abs card-link">SHOP NOW <svg width="16" height="8" viewBox="0 0 16 8" fill="none" stroke="#555"><path d="M0 4h15M11 1l4 3-4 3"/></svg></div>
</article>
<article class="abs card" style="left:863px;top:2500px">
  <div class="abs card-img" role="img" aria-label="Woman in an olive camisole and wide trousers" style="background:linear-gradient(180deg,#ededed,#7b6e5c 40%,#8a7c68)"></div>
  <div class="abs card-name">WOMEN CASUAL LINGERIE</div><div class="abs card-price">$49</div>
  <div class="abs card-link">SHOP NOW <svg width="16" height="8" viewBox="0 0 16 8" fill="none" stroke="#555"><path d="M0 4h15M11 1l4 3-4 3"/></svg></div>
</article>
<div class="abs pager" style="left:568px;top:2905px">
  <span><svg width="10" height="14" viewBox="0 0 10 14" fill="none" stroke="#fff" stroke-width="1.5"><path d="M8 1L2 7l6 6"/></svg></span>
  <span><svg width="10" height="14" viewBox="0 0 10 14" fill="none" stroke="#fff" stroke-width="1.5"><path d="M2 1l6 6-6 6"/></svg></span>
</div>

<!-- TESTIMONIALS -->
<section class="abs testi">
  <h2 class="abs center serif" style="top:76px;font-size:23px;font-weight:400;color:#222">WHAT CLIENTS SAY</h2>
  <p class="abs center" style="top:114px;font-size:10px;letter-spacing:2.5px;line-height:18px;color:#999">LOREM IPSUM DOLOR SIT AMET, CONSECTETUR ADIPISCING ELIT, SED DO EIUSMOD<br>TEMPOR INCIDIDUNT UT LABORE ET DOLORE MAGNA ALIQUA.</p>
  <div class="abs" role="img" aria-label="Client portrait" style="left:562px;top:210px;width:76px;height:76px;border-radius:50%;background:radial-gradient(circle,#d9b39c,#6b4a3a)"></div>
  <div class="abs center" style="top:326px;font-size:14px;letter-spacing:4px;color:#333">CLARA WINSLOW</div>
  <p class="abs center" style="top:358px;font-size:12.5px;font-style:italic;line-height:17px;color:#777">Lorem ipsum dolor sit amet, consec tetur adipis cing elit, sed do eiusmod tempor incid<br>idunt ut lab ore et dolore magna aliqua. Quis ipsum suspen di sse ultr ices gr avida. Risus<br>comm odo viverra maece nas accu msan lacus vel fac ilisis.</p>
  <svg class="abs" style="left:102px;top:325px" width="30" height="14" viewBox="0 0 30 14" fill="none" stroke="#333" stroke-width="1.5"><path d="M29 7H2M8 1L2 7l6 6"/></svg>
  <svg class="abs" style="left:1068px;top:325px" width="30" height="14" viewBox="0 0 30 14" fill="none" stroke="#333" stroke-width="1.5"><path d="M1 7h27M22 1l6 6-6 6"/></svg>
</section>

<!-- FOOTER -->
<footer class="abs footer">
  <div class="abs f-head" style="left:102px">QUICK LINKS</div>
  <ul class="abs f-list" style="left:102px">
    <li><svg width="12" height="6" viewBox="0 0 12 6" fill="none" stroke="#c8955a"><path d="M0 3h11M8 0.5L11 3 8 5.5"/></svg>ABOUT</li>
    <li><svg width="12" height="6" viewBox="0 0 12 6" fill="none" stroke="#c8955a"><path d="M0 3h11M8 0.5L11 3 8 5.5"/></svg>PRODUCTS</li>
    <li><svg width="12" height="6" viewBox="0 0 12 6" fill="none" stroke="#c8955a"><path d="M0 3h11M8 0.5L11 3 8 5.5"/></svg>BLOG</li>
    <li><svg width="12" height="6" viewBox="0 0 12 6" fill="none" stroke="#c8955a"><path d="M0 3h11M8 0.5L11 3 8 5.5"/></svg>SHOP</li>
    <li><svg width="12" height="6" viewBox="0 0 12 6" fill="none" stroke="#c8955a"><path d="M0 3h11M8 0.5L11 3 8 5.5"/></svg>CONTACT</li>
  </ul>
  <div class="abs f-head" style="left:308px">CATEGORIES</div>
  <ul class="abs f-list" style="left:308px">
    <li><svg width="12" height="6" viewBox="0 0 12 6" fill="none" stroke="#c8955a"><path d="M0 3h11M8 0.5L11 3 8 5.5"/></svg>WOMEN’S LINGERIE</li>
    <li><svg width="12" height="6" viewBox="0 0 12 6" fill="none" stroke="#c8955a"><path d="M0 3h11M8 0.5L11 3 8 5.5"/></svg>MEN’S LINGERIE</li>
    <li><svg width="12" height="6" viewBox="0 0 12 6" fill="none" stroke="#c8955a"><path d="M0 3h11M8 0.5L11 3 8 5.5"/></svg>FEATURED PRODUCTS</li>
    <li><svg width="12" height="6" viewBox="0 0 12 6" fill="none" stroke="#c8955a"><path d="M0 3h11M8 0.5L11 3 8 5.5"/></svg>POPULAR PRODUCTS</li>
    <li><svg width="12" height="6" viewBox="0 0 12 6" fill="none" stroke="#c8955a"><path d="M0 3h11M8 0.5L11 3 8 5.5"/></svg>ON SALE</li>
  </ul>
  <div class="abs f-head" style="left:531px">CONNTACT INFO</div>
  <ul class="abs f-list" style="left:531px">
    <li><svg width="16" height="16" viewBox="0 0 16 16" fill="none" stroke="#c8955a"><circle cx="8" cy="8" r="6.5"/><path d="M1.5 8h13M8 1.5c-3 3-3 10 0 13M8 1.5c3 3 3 10 0 13"/></svg>214 LINDEN GROVE AVENUE,</li>
    <li style="padding-left:26px">MAPLE HEIGHTS USA</li>
    <li><svg width="16" height="14" viewBox="0 0 16 14" fill="none" stroke="#c8955a"><rect x="1" y="2" width="14" height="10"/><path d="M1 2l7 6 7-6"/></svg>HELLO@VELORACASA.COM</li>
    <li style="padding-top:12px"><svg width="16" height="14" viewBox="0 0 16 14" fill="none" stroke="#c8955a"><rect x="1" y="1" width="14" height="10"/><path d="M4 11v3l3-3M4 5h8M4 8h5"/></svg>1-5550-132, &nbsp;&nbsp;&nbsp;1-555-0187</li>
  </ul>
  <div class="abs f-head" style="left:812px">JOIN NEWLETTER</div>
  <p class="abs" style="left:812px;top:136px;width:290px;font-size:9.5px;letter-spacing:1.2px;line-height:17px">LOREM IPSUM DOLOR SIT AMET , CONSECTETUR ADIPIS CING ELIT, SED DO EIUSMOD TEM POR INCI DIDUNT UT LAB ORE ET DO LORE.</p>
  <div class="abs" style="left:812px;top:200px;width:283px;height:42px;background:#fff"></div>
  <a class="abs btn-gold" style="left:983px;top:264px;width:112px;height:41px;font-size:11px;letter-spacing:2px">SUBSCRIBE</a>
  <div class="abs" style="left:0;top:335px;width:1200px;height:1px;background:#44444f"></div>
  <div class="abs center" style="top:357px;font-size:10px;letter-spacing:2.5px">ALLRIGHTS RESERVED FOR VELORA CASA</div>
</footer>

</body>
</html>
```